依頼詳細
ポスティングや駅などでの手渡しで活用するためのチラシ作成をお願いいたします。

〇絶対に記載いただきたい内容(意図が伝わるなら文字が変わっても良いです)
1)ヤネルやリブナス、ベルクエスト等に掲載されている物件も含め、全ての物件で仲介手数料無料
2)不動産屋は基本的に全国どこの物件も仲介が出来る
3)駐車場の管理費無料
4)売買物件も得意(投資家や一般の方向けのどちらでも)
5)どこの不動産屋よりも誠実でありたい
記載項目
社名:(不動産のミルベリー)
電話番号:092-555-0183
URL:https://www.milberry.co.jp/home
サービス内容:賃貸仲介、売買仲介、物件管理、駐車場管理
※その他として、依頼詳細で書いた内容は入れていただけましたら幸いです。
※カフェも経営しているという内容。
参考にカフェのページも記載させていただきます。
https://www.milberry.co.jp/

それと福岡にある仲介手数料無料とうたっている***他社サイトを記載します。

1
https://www.sunvale-fukuoka.jp/
2
https://www.palmtree-f.co.jp/
3
https://hoshizora-chintai.com/#
4
https://www.vela-nest.co.jp/

-----------------------------------------
サイズ
A4
ページ数
片面
希望イメージ
シンプル 複雑
単色 カラフル
暗い 明るい
日常 高級
遊び心 厳粛
未来的 伝統的
女性的 男性的
希望する色
赤系、黄・オレンジ系
納品ファイル
• 高解像度JPG (.jpg)
• イラストレーター形式 (.ai)
• フォトショップ形式 (.psd)
• PNG形式 (.png)
補足説明
■ 選んだ理由

この度はとても素敵なご提案を頂きまして、誠に有難うございました。
手直しもお願いがあり大変恐縮ではございますが、何卒ご対応を頂けましたら幸いです。

■ 提案者全員のお礼・コメント

沢山のご提案を頂き誠に有難うございました。
非常に悩ましいくらい良いご提案ばかりでございました。
またご依頼をさせていただくとは思いますので、その際はまた是非ご協力を頂けましたら幸いです。

```html
<!DOCTYPE html>
<html lang="ja">
<head>
<meta charset="utf-8">
<title>不動産のミルベリー 仲介手数料完全無料</title>
<link rel="stylesheet" href="https://fonts.googleapis.com/css2?family=Noto+Sans+JP:wght@500;700;900&family=Roboto:wght@700;900&display=swap">
<style>
:root{
  --navy:#1d2b5c;
  --red:#e0202a;
  --yellow:#ffe100;
  --sky:#dceefa;
  --white:#ffffff;
  --ink:#222;
}
*{margin:0;padding:0;box-sizing:border-box}
html,body{width:848px;height:1200px;overflow:hidden;background:#fff}
body{font-family:"Noto Sans JP",sans-serif;color:var(--ink)}
.flyer{position:relative;width:848px;height:1200px;overflow:hidden;background:var(--white)}
.hero{position:absolute;left:0;top:0;width:848px;height:460px;background:linear-gradient(180deg,#eaf5fd,var(--sky))}
.abs{position:absolute}
.tagline{left:110px;top:22px;width:520px;height:44px;border:3px solid var(--navy);border-radius:8px;background:#fff;color:var(--navy);font-weight:700;font-size:20px;white-space:nowrap;display:flex;align-items:center;justify-content:center}
.staff-woman{left:660px;top:0;width:150px;height:112px;border-radius:0 0 75px 75px;background:linear-gradient(180deg,#c9d7e6,#8fa6c2)}
.listing-line{left:40px;color:var(--navy);font-weight:900;font-size:38px;letter-spacing:1px;line-height:1;white-space:nowrap}
.listing-line.l1{top:84px}
.listing-line.l2{top:132px}
.listing-line em{font-style:normal;color:var(--red)}
.outline{paint-order:stroke fill;white-space:nowrap}
.fee{left:38px;top:176px;font-size:100px;font-weight:900;color:var(--red);-webkit-text-stroke:12px var(--white);line-height:1;letter-spacing:2px}
.badge{left:680px;top:122px;width:140px;height:140px;border-radius:50%;background:#fff;border:4px solid var(--red);color:var(--red);font-weight:900;font-size:20px;line-height:1.25;display:flex;align-items:center;justify-content:center;text-align:center}
.scope{left:42px;top:285px;width:220px;height:110px;background:var(--navy);color:#fff;font-weight:900;font-size:32px;line-height:1.25;display:flex;flex-direction:column;align-items:center;justify-content:center}
.scope span:first-child{color:var(--yellow);font-size:28px}
.free{left:272px;top:276px;font-size:118px;font-weight:900;color:var(--yellow);-webkit-text-stroke:14px var(--navy);line-height:1;letter-spacing:2px}
.ribbon{left:0;top:402px;width:848px;height:50px;z-index:2}
.ribbon-text{left:0;top:402px;width:848px;height:50px;display:flex;align-items:center;justify-content:center;font-weight:900;font-size:26px;color:var(--red);z-index:3;white-space:nowrap}
.city-photo{left:0;top:452px;width:848px;height:496px;background:linear-gradient(180deg,#a9cdec 0%,#cfe2f0 30%,#b9b9b0 60%,#8e9a86 100%)}
.parking{left:24px;top:560px;width:240px;height:220px}
.parking-text{left:24px;top:560px;width:240px;height:220px;display:flex;flex-direction:column;align-items:center;justify-content:center;color:var(--red);font-weight:900;font-size:30px;line-height:1.25;text-align:center}
.sales{left:268px;top:716px;width:196px;height:196px;border-radius:50%;background:#fff;border:4px solid var(--red);display:flex;flex-direction:column;align-items:center;justify-content:center;text-align:center}
.sales .who{color:var(--red);font-weight:700;font-size:19px;line-height:1.3}
.sales .what{color:var(--red);font-weight:900;font-size:32px;line-height:1.2;margin-top:4px}
.message{left:458px;top:537px;width:220px;height:270px;background:rgba(255,255,255,.95);padding:14px 14px;font-size:14px;line-height:1.75;font-weight:500;color:var(--ink)}
.message b{color:var(--red);font-weight:900}
.staff-man{left:680px;top:680px;width:160px;height:268px;border-radius:80px 80px 0 0;background:linear-gradient(180deg,#b8c4d2,#6f7f95)}
.sincere{left:40px;top:954px;color:var(--navy);font-weight:900;font-size:37px;letter-spacing:1px;white-space:nowrap}
.brand-row{left:40px;top:1004px;display:flex;align-items:center;gap:20px}
.brand-name{color:var(--navy);font-weight:900;font-size:38px;white-space:nowrap}
.services{border:2px solid var(--navy);color:var(--navy);font-weight:700;font-size:14px;line-height:1.5;padding:4px 10px}
.logo{left:40px;top:1068px;width:240px;display:flex;align-items:center;gap:10px}
.logo-mark{width:26px;height:26px;background:var(--navy)}
.logo-name{font-family:"Noto Sans JP",sans-serif;font-weight:900;font-size:28px;color:var(--navy);letter-spacing:2px}
.tel{left:300px;top:1054px;color:var(--red);font-family:"Roboto",sans-serif;font-weight:900;font-size:48px;line-height:1;white-space:nowrap}
.tel small{font-size:26px;margin-right:6px}
.url{left:300px;top:1108px;color:var(--navy);font-weight:700;font-size:20px;line-height:1.3;white-space:nowrap}
.access{left:40px;top:1140px;color:var(--navy);font-weight:700;font-size:14px;line-height:1.4;white-space:nowrap}
.address{left:370px;top:1141px;font-size:12px;line-height:1.5;font-weight:500;color:var(--ink);white-space:nowrap}
.cafe-band{left:0;top:1166px;width:848px;height:34px;background:var(--navy);color:#fff;font-weight:700;font-size:18px;display:flex;align-items:center;justify-content:center;gap:8px;white-space:nowrap}
.cafe-band .link{color:var(--yellow)}
</style>
</head>
<body>
<main class="flyer">
  <section class="hero"></section>

  <p class="abs tagline">福岡でイチバンの誠実対応、信頼の不動産屋です!</p>
  <div class="abs staff-woman" role="img" aria-label="笑顔で案内するスーツ姿の女性スタッフのイラスト"></div>

  <p class="abs listing-line l1"><em>ヤネル</em>や<em>リブナス</em>、<em>ベルクエスト</em></p>
  <p class="abs listing-line l2">等に掲載されている物件も含め</p>

  <h1 class="abs fee outline">仲介手数料</h1>
  <p class="abs badge">お客様の<br>ために<br>限界に<br>挑戦!</p>

  <p class="abs scope"><span>福岡市内</span><span>全ての物件</span></p>
  <p class="abs free outline">完全無料</p>

  <svg class="abs ribbon" viewBox="0 0 848 50" aria-hidden="true">
    <polygon points="0,0 848,0 828,25 848,50 0,50 20,25" fill="#ffe100"/>
  </svg>
  <p class="abs ribbon-text">＼ 不動産屋は基本的に全国どこの物件も仲介が出来ます! ／</p>

  <div class="abs city-photo" role="img" aria-label="福岡市の住宅街とマンションが広がる街並みの写真"></div>

  <svg class="abs parking" viewBox="0 0 240 220" aria-hidden="true">
    <polygon fill="#ffe100" stroke="#e0202a" stroke-width="3" points="120,4 140,30 172,12 176,46 212,40 200,74 236,86 206,108 232,134 196,142 206,178 170,170 164,208 134,186 120,216 106,186 76,208 70,170 34,178 44,142 8,134 34,108 4,86 40,74 28,40 64,46 68,12 100,30"/>
  </svg>
  <p class="abs parking-text"><span>駐車場の</span><span>管理費も</span><span>全て無料!</span></p>

  <div class="abs sales">
    <p class="who">投資家の方<br>一般の方</p>
    <p class="what">売買物件<br>も得意!</p>
  </div>

  <p class="abs message">私達は創業以来、地域の皆様に寄り添い続けてきました。<b>仲介手数料無料</b>で、住まい探しの負担を少しでも軽くしたい。その想いで日々誠実に取り組んでいます。賃貸も売買も、どんな物件でもまずはお気軽にご相談ください。</p>

  <div class="abs staff-man" role="img" aria-label="案内するスーツ姿の男性スタッフのイラスト"></div>

  <p class="abs sincere">どこの不動産屋よりも誠実でありたい</p>
  <div class="abs brand-row">
    <p class="brand-name">不動産のミルベリー</p>
    <p class="services">賃貸仲介/売買仲介/<br>物件管理/駐車場管理</p>
  </div>

  <div class="abs logo">
    <span class="logo-mark"></span>
    <span class="logo-name">MILBERRY</span>
  </div>
  <p class="abs tel"><small>TEL.</small>092-555-0183</p>
  <p class="abs url">URL : https://www.milberry.co.jp/home</p>
  <p class="abs access">大濠公園から1番近い不動産屋(徒歩1分)</p>
  <p class="abs address">〒810-0099 福岡市中央区港町2丁目4-5</p>

  <p class="abs cafe-band">★本格コーヒー&amp;スイーツのカフェも併設しております★ <span class="link">https://www.milberry.co.jp/</span></p>
</main>
</body>
</html>
```